Letterhead

We are looking for a basic letterhead. It should include our logo, website - northpeakkitchenware.com, phone 907.418.3952, toll free 855.392.6180, and fax 907.418.5263, along with our address 4837 Birchwood Lane, Anchorage, AK 99517. I want something that will look good printed in color or black and white.

```html
<!DOCTYPE html>
<html lang="en">
<head>
<meta charset="utf-8">
<title>North Peak Kitchenware Letterhead</title>
<link rel="stylesheet" href="https://fonts.googleapis.com/css2?family=Arimo:wght@400;700&family=Signika:wght@300;400&display=swap">
<style>
  :root {
    --backdrop: #e6e6e6;
    --paper: #ffffff;
    --brand-blue: #1f3f8f;
    --brand-red: #c8303f;
    --accent-blush: #e0a39b;
    --ink: #1c1c1c;
    --signature-ink: #7c8ec4;
  }
  * { margin: 0; padding: 0; box-sizing: border-box; }
  html, body {
    width: 935px; height: 1200px; overflow: hidden;
    background: var(--backdrop);
  }
  .letterhead {
    position: absolute; left: 67px; top: 82px;
    width: 800px; height: 1035px;
    background: var(--paper);
    overflow: hidden;
    box-shadow: 0 2px 10px rgba(0,0,0,0.12);
  }
  .brand-name {
    position: absolute; left: 36px; top: 62px;
    display: flex; align-items: center; gap: 12px;
    font-family: "Arimo", Arial, sans-serif;
    font-weight: 700; font-size: 30px; line-height: 1.1;
    color: var(--brand-blue);
  }
  .brand-name .brand-square {
    width: 22px; height: 22px; background: var(--brand-blue);
  }
  .contact-bar {
    position: absolute; left: 525px; top: 40px;
    width: 18px; height: 116px; background: var(--brand-red);
  }
  .contact-details {
    position: absolute; left: 552px; top: 36px;
    font-family: "Arimo", Arial, sans-serif;
    font-size: 15px; line-height: 21px;
    color: var(--brand-blue);
    list-style: none;
  }
  .contact-details .address { margin-top: 2px; }
  .salutation {
    position: absolute; left: 102px; top: 312px;
    font-family: "Signika", "Trebuchet MS", sans-serif;
    font-weight: 400; font-size: 25px; color: var(--ink);
  }
  .letter-body {
    position: absolute; left: 102px; top: 392px; width: 596px;
    font-family: "Signika", "Trebuchet MS", sans-serif;
    font-weight: 300; font-size: 13.6px; line-height: 22px;
    color: var(--ink); text-align: justify;
  }
  .letter-body p + p { margin-top: 22px; }
  .closing {
    position: absolute; right: 102px; top: 804px;
    font-family: "Signika", "Trebuchet MS", sans-serif;
    font-weight: 300; font-size: 13.6px; color: var(--ink);
  }
  .signature {
    position: absolute; left: 580px; top: 875px;
    width: 135px; height: 40px;
    background: var(--signature-ink); opacity: 0.25; border-radius: 4px;
  }
  .accent-band {
    position: absolute; left: 0; top: 0;
  }
</style>
</head>
<body>
  <main class="letterhead">
    <svg class="accent-band" width="800" height="1035" viewBox="0 0 800 1035" aria-hidden="true">
      <polygon points="375,1035 800,862 800,950 580,1035" fill="var(--accent-blush)"/>
    </svg>

    <div class="brand-name"><span class="brand-square"></span>NORTH PEAK KITCHENWARE</div>

    <div class="contact-bar"></div>
    <ul class="contact-details">
      <li>Www.northpeakkitchenware.com</li>
      <li>Phone 907.418.3952</li>
      <li>Toll free 855.392.6180</li>
      <li>Fax 907.418.5263</li>
      <li class="address">Address 4837 Birchwood Lane,</li>
      <li>Anchorage, AK 99517</li>
    </ul>

    <h1 class="salutation">Dear Mr. Callahan,</h1>

    <section class="letter-body">
      <p>Lorem ipsum dolor sit amet, consectetur adipiscing elit. Donec orci purus, luctus vitae dignissim eu, iaculis sed purus. Vivamus faucibus, ipsum nec aliquet viverra, leo mauris condimentum ligula, sit amet sagittis enim ligula quis arcu. Nam egestas tortor id nisi porttitor mattis. In tortor ante, ultricies in suscipit a, tempus non massa. Vivamus et auctor mi. Fusce vel massa nulla. Phasellus nec eros mauris, et scelerisque orci.</p>
      <p>Donec malesuada orci vitae nulla accumsan porta a id massa. Quisque accumsan iaculis magna sit amet fringilla. Maecenas consequat, magna eget tincidunt semper, odio nibh rutrum mi, id feugiat ante nisi eu risus. Vestibulum nunc orci, rhoncus a placerat in, ultricies in mi. Cras mattis varius eros, vel fringilla nisi suscipit eget. Quisque scelerisque sagittis nulla at porttitor.</p>
      <p>Sed id augue vitae urna euismod commodo aliquet a quam. Pellentesque arcu velit, cursus et malesuada ut, consequat et diam. Nullam erat sem, rhoncus id ullamcorper vitae, rhoncus et arcu. In ultricies ultricies nulla, ut rutrum nisi iaculis at. Donec eu magna a metus ornare faucibus. Fusce aliquet faucibus ultricies. Morbi semper, est id tincidunt gravida, sem arcu adipiscing lacus, ac bibendum nulla leo eu purus. Quisque nec diam sed risus consectetur a ccumsan quis quis nibh. Vestibulum id purus lorem.</p>
    </section>

    <p class="closing">Sincerely,</p>
    <div class="signature" role="img" aria-label="Handwritten signature of Dana Reyes"></div>
  </main>
</body>
</html>
```